Wendlow Superfoods Packaging Design

We are looking for a design for our premium superfoods powders and blends. Packaging dimensions are 21cm x 13cm Kraft packaging (light brown background). This design should be a blueprint for other products that we will be marketing including lions mane mushroom, reishi mushroom, Chaga mushroom, Spirilina, bee pollen, açai powder and the like. The design should be clean but earthy, and the template replicable for other products.

```html
<!DOCTYPE html>
<html lang="en">
<head>
<meta charset="UTF-8">
<title>Wendlow Superfoods – Moringa Leaf Pouch</title>
<link href="https://fonts.googleapis.com/css2?family=Montserrat:wght@500;600;800;900&family=Lato:wght@400;700;900&display=swap" rel="stylesheet">
<style>
  :root {
    --bg: #83f5b9;
    --forest: #1f4d1a;
    --forest-deep: #173d13;
    --leaf: #2f7d2b;
    --paper: #e6e7e6;
    --ink: #141414;
    --gold: #c9a21b;
    --white: #ffffff;
  }
  * { margin: 0; padding: 0; box-sizing: border-box; }
  html, body { width: 1200px; height: 1200px; overflow: hidden; background: var(--bg); }
  .canvas { position: relative; width: 1200px; height: 1200px; }
  .pouch {
    position: absolute; left: 300px; top: 130px; width: 600px; height: 940px;
    background: var(--forest); overflow: hidden;
  }
  .pouch-art { position: absolute; inset: 0; }
  .zip-line { position: absolute; left: 20px; right: 20px; height: 4px; background: var(--forest-deep); }
  .brand { position: absolute; left: 0; right: 0; top: 250px; text-align: center; color: var(--ink); font-family: "Montserrat", sans-serif; font-weight: 500; }
  .brand-name { font-size: 78px; letter-spacing: 1px; line-height: 1; }
  .brand-rule { width: 370px; height: 2px; background: #333; margin: 22px auto 8px; }
  .brand-sub { font-size: 20px; letter-spacing: 4px; }
  .product-title {
    position: absolute; left: 0; right: 0; top: 395px; text-align: center;
    font-family: "Montserrat", sans-serif; font-weight: 900; color: var(--forest); line-height: 1;
  }
  .product-title .line-1 { font-size: 84px; letter-spacing: -1px; }
  .product-title .line-2 { display: flex; align-items: center; justify-content: center; gap: 14px; font-size: 76px; margin-top: 2px; }
  .title-stripes { display: flex; flex-direction: column; gap: 6px; width: 130px; }
  .title-stripes span { height: 6px; background: var(--ink); }
  .intro {
    position: absolute; left: 60px; right: 60px; top: 566px; text-align: center;
    font-family: "Lato", sans-serif; font-weight: 900; font-size: 13px; line-height: 1.2; color: var(--ink);
  }
  .info-panel { position: absolute; left: 18px; right: 14px; top: 640px; height: 175px; background: var(--forest); z-index: 2; }
  .benefits { position: absolute; left: 36px; top: 12px; list-style: none; font-family: "Lato", sans-serif; font-size: 13.5px; letter-spacing: 0.6px; color: var(--white); }
  .benefits li { display: flex; gap: 10px; align-items: center; height: 38px; line-height: 1.1; }
  .benefits svg { flex: none; }
  .description {
    position: absolute; right: 16px; top: 10px; width: 230px; text-align: center;
    font-family: "Lato", sans-serif; font-size: 11.5px; line-height: 1.15; letter-spacing: 0.3px; color: #e9efe8;
  }
  .lower-band { position: absolute; left: 18px; right: 14px; top: 815px; height: 110px; background: var(--ink); }
  .badge-band { position: absolute; right: 0; top: 10px; width: 230px; height: 100px; background: var(--paper); }
  .weight-badge {
    position: absolute; left: 45px; top: 10px; width: 44px; height: 44px; border: 2px solid #333; border-radius: 50%;
    display: flex; align-items: center; justify-content: center; font-family: "Lato", sans-serif; font-size: 12px; color: #222;
  }
  .cert { position: absolute; border-radius: 50%; background: var(--leaf); }
  .cert.square { border-radius: 4px; background: none; border: 2px solid var(--leaf); }
  .leaf-art {
    position: absolute; left: 110px; top: 820px; width: 230px; height: 105px; border-radius: 50% 40% 50% 40%;
    background: radial-gradient(ellipse at 55% 45%, #3f8f33 0%, #2a6a22 60%, rgba(20,50,16,0) 100%);
  }
  .base-strip { position: absolute; left: 18px; right: 14px; bottom: 0; height: 15px; background: var(--ink); }
</style>
</head>
<body>
<main class="canvas">
  <section class="pouch">
    <div class="zip-line" style="top:72px"></div>
    <div class="zip-line" style="top:92px"></div>
    <div class="zip-line" style="top:112px"></div>

    <svg class="pouch-art" width="600" height="940" viewBox="0 0 600 940" aria-hidden="true">
      <path d="M0,222 C120,182 210,160 305,160 C420,160 520,220 600,300 L600,815 L0,815 Z" fill="var(--paper)"/>
      <path d="M0,214 C120,174 210,152 305,152 C420,152 520,212 600,292" fill="none" stroke="var(--gold)" stroke-width="7"/>
      <path d="M0,205 C120,165 210,143 305,143 C420,143 520,203 600,283" fill="none" stroke="var(--ink)" stroke-width="3"/>
      <path d="M0,222 C120,182 210,160 305,160 C420,160 520,220 600,300" fill="none" stroke="var(--ink)" stroke-width="3"/>
    </svg>

    <header class="brand">
      <div class="brand-name">Wendlow</div>
      <div class="brand-rule"></div>
      <div class="brand-sub">SUPERFOODS</div>
    </header>

    <h1 class="product-title">
      <div class="line-1">MORINGA</div>
      <div class="line-2">
        <span class="title-stripes"><span></span><span></span><span></span></span>
        LEAF
        <span class="title-stripes"><span></span><span></span><span></span></span>
      </div>
    </h1>

    <p class="intro">MORINGA, ALSO KNOWN AS ‘THE MIRACLE TREE’, HAS BEEN PRAISED FOR IT’S HEALTH BENEFITS FOR THOUSANDS OF YEARS. IT IS EXTREMELY RICH IN HEALTHY ANTIOXIDANTS AND BIOACTIVE COMPOUNDS. IF FACT IT HAS:</p>

    <div class="info-panel">
      <ul class="benefits">
        <li><svg width="30" height="30" viewBox="0 0 30 30"><circle cx="14" cy="16" r="11" fill="none" stroke="#fff" stroke-width="2.5"/><path d="M8 15 l5 5 L27 5" fill="none" stroke="#fff" stroke-width="3"/></svg><span>7x THE VITAMIN C<br>OF ORANGES</span></li>
        <li><svg width="30" height="30" viewBox="0 0 30 30"><circle cx="14" cy="16" r="11" fill="none" stroke="#fff" stroke-width="2.5"/><path d="M8 15 l5 5 L27 5" fill="none" stroke="#fff" stroke-width="3"/></svg><span>3x THE POTASSIUM<br>OF BANANAS</span></li>
        <li><svg width="30" height="30" viewBox="0 0 30 30"><circle cx="14" cy="16" r="11" fill="none" stroke="#fff" stroke-width="2.5"/><path d="M8 15 l5 5 L27 5" fill="none" stroke="#fff" stroke-width="3"/></svg><span>4x THE CALCIUM<br>OF MILK</span></li>
        <li><svg width="30" height="30" viewBox="0 0 30 30"><circle cx="14" cy="16" r="11" fill="none" stroke="#fff" stroke-width="2.5"/><path d="M8 15 l5 5 L27 5" fill="none" stroke="#fff" stroke-width="3"/></svg><span>3x IRON OF<br>SPINICH</span></li>
      </ul>
      <p class="description">The Leaves Contain All Nine Essential Amino Acids And Traditionally Used In Assisting The Healing Of Many Ailments. The Nutiritional Diveristy Is Also Known To Reduce Both Cholesterol And Blood Sugar Levels Whilst And Have Serious Anti-inflammatory Benefits. Our 100% Organic Moringa Is Grown And Harvested In It’s Native Enviornment, Supporting Premium Superfood Nutrition.</p>
    </div>

    <div class="lower-band">
      <div class="badge-band">
        <div class="weight-badge">250g</div>
        <div class="cert" style="left:105px;top:8px;width:46px;height:46px;"></div>
        <div class="cert" style="left:6px;top:58px;width:42px;height:38px;"></div>
        <div class="cert" style="left:60px;top:56px;width:44px;height:42px;"></div>
        <div class="cert square" style="left:118px;top:62px;width:58px;height:32px;"></div>
      </div>
    </div>

    <div class="leaf-art" role="img" aria-label="Illustration of a sprig of green moringa leaves"></div>
    <div class="base-strip"></div>
  </section>
</main>
</body>
</html>
```